School Initiative to begin applied Design Thinking Projects

We have a corporate logo and a symbole with are the three gears. We primarily focus on the gear's colors pink, blue and green. However, the school's colors are Black and Red. The design should be have introductory sections with case studies, about us blank pages, methodology and tools, process map, page for unique selling point, Compare and contrast page . The design should be rather simple don't allow for many words, key words should pop out
Updates

Please refer to our parent brand. We are separate but there should be some connectivity

http://www.velbrook.quarnell-uni.example/FacultyAndResearch/EducationCentres/FormLabs/AboutBD.aspx

Target Market(s)

Clients who are unexposed to this type of thinking so there should be rooms for pictures and explanation and the design must capture their attention

Industry/Entity Type

School

Requirements
Must have
• Corporate Logo on the cover pages with the three gears "zentrix business design'
Separate pages going into more detail do not need the three gears

The footer should have indicator of where along the ppt slide we are on
ex. Introduction ...Gear 1....Gear 2....Gear 3....About Us....About Harrowvale Polytechnic
Nice to have
• Graphics to represent different tools, research, fieldwork, interviews, strategy, needs finding, journey mapping

I need a page to describe a project, I'll upload a sample with the content that it should have. Many Thanks!

Also included are some older files about business design, I dpn't know the syle but some of the formatting might be useful

```html
<!DOCTYPE html>
<html lang="en">
<head>
<meta charset="utf-8">
<title>Gears of Business Design – Slides</title>
<link href="https://fonts.googleapis.com/css2?family=Roboto:wght@300;400;500;700&display=swap" rel="stylesheet">
<style>
  :root {
    --stage: #262626;
    --ink: #1e1e1e;
    --muted: #8a8a8a;
    --school-red: #b3101a;
    --school-black: #000000;
    --gear-pink: #e2478f;
    --gear-blue: #2a9ddc;
    --gear-green: #8cc43f;
    --slide-top: #f4f6f7;
    --slide-bottom: #e6ecef;
  }
  * { box-sizing: border-box; margin: 0; padding: 0; }
  html, body { width: 1200px; height: 1200px; overflow: hidden; }
  body {
    background: var(--stage);
    font-family: "Roboto", Arial, sans-serif;
    color: var(--ink);
    position: relative;
  }
  .slide {
    position: absolute;
    left: 240px;
    width: 720px;
    height: 451px;
    background:
      radial-gradient(circle at 85% 75%, rgba(140,196,63,0.08), transparent 35%),
      radial-gradient(circle at 85% 18%, rgba(226,71,143,0.07), transparent 25%),
      radial-gradient(circle at 30% 30%, #ffffff, transparent 55%),
      linear-gradient(180deg, var(--slide-top), var(--slide-bottom));
    overflow: hidden;
  }
  .slide--overview { top: 58px; }
  .slide--detail { top: 569px; }
  .slide__topbar {
    position: absolute; left: 0; top: 0; width: 100%; height: 4px;
    background: var(--school-black);
  }
  .slide-title {
    position: absolute; left: 82px; top: 34px;
    display: flex; align-items: center; gap: 3px;
  }
  .slide-title__number {
    color: var(--school-red); font-size: 38px; font-weight: 500; line-height: 1;
  }
  .slide-title__words {
    font-size: 19px; font-weight: 300; line-height: 0.9; color: #333;
  }
  .intro-copy {
    position: absolute; left: 108px; top: 89px; width: 540px;
    font-size: 9.6px; line-height: 17px; color: #333;
  }
  .gear-diagram {
    position: absolute; left: 238px; top: 156px; width: 228px; height: 226px;
    border-radius: 50%;
    background: radial-gradient(circle at 45% 40%, rgba(42,157,220,0.25), rgba(140,196,63,0.22) 55%, rgba(226,71,143,0.05) 75%, transparent 76%);
  }
  .stage-label { position: absolute; }
  .stage-label__name { font-size: 15px; font-weight: 700; line-height: 16px; }
  .stage-label__question { font-size: 11.5px; line-height: 12.5px; color: #333; margin-top: 2px; }
  .stage-label--empathy { left: 395px; top: 156px; }
  .stage-label--empathy .stage-label__name { color: var(--gear-pink); }
  .stage-label--empathy .stage-label__question { margin-top: 4px; }
  .stage-label--concept { right: 499px; top: 211px; text-align: right; }
  .stage-label--concept .stage-label__name { color: var(--gear-blue); }
  .stage-label--strategy { left: 484px; top: 311px; }
  .stage-label--strategy .stage-label__name { color: var(--gear-green); }

  .section-heading {
    position: absolute; left: 285px; top: 106px;
    font-size: 13px; font-weight: 700; color: var(--gear-blue);
  }
  .picture-slot {
    position: absolute; left: 83px; top: 142px; width: 166px; height: 166px;
    background: #ffffff; border: 1px solid #d8dcde;
    box-shadow: 0 0 3px rgba(0,0,0,0.08);
    display: flex; align-items: center; justify-content: center;
    font-size: 9px; color: #bbb;
  }
  .body-copy {
    position: absolute; left: 285px; top: 139px; width: 356px;
    font-size: 9.7px; line-height: 13.6px; color: #333;
  }
  .body-copy p + p { margin-top: 13.6px; }

  .slide-footer { position: absolute; left: 0; top: 421px; width: 100%; height: 30px; }
  .slide-footer__bar {
    position: absolute; top: 2px; height: 16px;
    background: var(--school-black); border-top: 1.5px solid var(--school-red);
  }
  .slide-footer__bar--left { left: 0; width: 78px; }
  .slide-footer__bar--middle {
    left: 267px; width: 330px;
    color: #fff; font-size: 9.6px; line-height: 14px; padding: 0 20px;
  }
  .slide-footer__bar--middle.is-right { text-align: right; padding-right: 6px; font-weight: 500; letter-spacing: 0.2px; }
  .slide-footer__bar--right { left: 649px; width: 71px; }
  .slide-footer__mark {
    position: absolute; left: 86px; top: 3px; width: 16px; height: 16px;
    border-radius: 50%; background: var(--gear-green);
  }
  .slide-footer__section {
    position: absolute; left: 114px; top: 1px;
    font-size: 15px; font-weight: 700; color: var(--school-red);
  }
  .slide-footer__divider {
    position: absolute; left: 215px; top: 3px; width: 1px; height: 14px; background: #ccc;
  }
  .slide-footer__step {
    position: absolute; left: 225px; top: 5px; font-size: 11px; color: var(--muted);
  }
  .slide-footer__page { position: absolute; left: 599px; top: -2px; white-space: nowrap; }
  .slide-footer__page small { font-size: 7.5px; color: #333; }
  .slide-footer__page strong { font-size: 19px; font-weight: 700; color: var(--school-red); }
</style>
</head>
<body>

<section class="slide slide--overview">
  <div class="slide__topbar"></div>
  <h1 class="slide-title">
    <span class="slide-title__number">3</span>
    <span class="slide-title__words">Gears of<br>Business Design</span>
  </h1>
  <p class="intro-copy">The Business Design methodology begins with an understanding of what customers really need. This is followed by a broad exploration of new solutions and culminates with a business strategy that creates competitive advantage.</p>

  <div class="gear-diagram" role="img" aria-label="Three interlocking gears in pink, blue and green representing the stages of business design"></div>

  <div class="stage-label stage-label--empathy">
    <div class="stage-label__name">Empathy &amp; Deep Human<br>Understanding</div>
    <div class="stage-label__question">What is the unmet need?</div>
  </div>
  <div class="stage-label stage-label--concept">
    <div class="stage-label__name">Concept<br>Visualization</div>
    <div class="stage-label__question">How might we better<br>meet that need?</div>
  </div>
  <div class="stage-label stage-label--strategy">
    <div class="stage-label__name">Strategic<br>Business Design</div>
    <div class="stage-label__question">How do we design<br>the business to win?</div>
  </div>

  <footer class="slide-footer">
    <div class="slide-footer__bar slide-footer__bar--left"></div>
    <span class="slide-footer__mark"></span>
    <span class="slide-footer__section">Introduction</span>
    <span class="slide-footer__divider"></span>
    <span class="slide-footer__step">Gear 1</span>
    <div class="slide-footer__bar slide-footer__bar--middle">Name of Project write here</div>
    <span class="slide-footer__page"><small>Page</small> <strong>2</strong></span>
    <div class="slide-footer__bar slide-footer__bar--right"></div>
  </footer>
</section>

<section class="slide slide--detail">
  <div class="slide__topbar"></div>
  <h1 class="slide-title">
    <span class="slide-title__number">3</span>
    <span class="slide-title__words">Gears of<br>Business Design</span>
  </h1>
  <h2 class="section-heading">Concept Visualization</h2>
  <div class="picture-slot">Insert Picture</div>
  <div class="body-copy">
    <p>This is just dummy text. You can replace it later. BUSINESS DESIGN is a human-centred approach to creative problem solving. It applies design methods and mindsets to business challenges. It can be effectively used to help better understand customers, create new experiences and design innovative business strategies and models.</p>
    <p>Collaboratively administrate empowered markets via plug-and-play networks. Dynamically procrastinate B2C users after installed base benefits. Dramatically visualize customer directed convergence without revolutionary ROI.</p>
    <p>Efficiently unleash cross-media information without cross-media value. Quickly maximize timely deliverables for real-time schemas. Dramatically maintain clicks-and-mortar solutions without functional solutions. Completely synergize resource sucking relationships via premier niche markets. Professionally cultivate one-to-one customer service with robust ideas. Dynamically</p>
  </div>

  <footer class="slide-footer">
    <div class="slide-footer__bar slide-footer__bar--left"></div>
    <span class="slide-footer__mark"></span>
    <span class="slide-footer__section">Introduction</span>
    <span class="slide-footer__divider"></span>
    <span class="slide-footer__step">Gear 2</span>
    <div class="slide-footer__bar slide-footer__bar--middle is-right">HARROWVALE POLYTECHNIC</div>
    <span class="slide-footer__page"><small>Page</small> <strong>3</strong></span>
    <div class="slide-footer__bar slide-footer__bar--right"></div>
  </footer>
</section>

</body>
</html>
```